СРОЧНО! Дизайн линейки кондитерских десертов
Задание на дизайн
Приоритеты объектов в упаковке
Знак производителя, Марка продукта, Вид продукта, Иллюстрация
Опишите свою организацию или продукт и целевую аудиторию
Продукция будет представлена в крупных розничных сетях. Свежий многослойный десерт в квадратной прозрачной упаковке с крышечкой.
Вес 100-140 грамм в зависимости от вида, идеально для удобного индивидуального потребления на один раз.
Бренд привлекает широкую целевую аудиторию потребителей тортов и пирожных. Если потребление семейное, то каждый может выбрать свой любимый вкус. Подходит для потребления дома, в дороге или на работе, а также как перекус с чашкой чая или кофе или десерт после еды или вечернее лакомство.
Приложите логотипы или другие материалы
Порционное пирожное в квадратном стакане с крышкой
Необходимо создать дизайн-макет для картонной обечайки. Размеры: верх - 40х65, бок - 40х70 мм
концепты-аналоги, которые уже есть в продаже
Комментарии и пожелания для дизайнеров
Задача создать дизайн для линейки кондитерских пирожных в классических вкусах для продажи в современной рознице на примере дизайна для вкуса ТИРАМИСУ. Линейка классических вкусов Тирамису, Медовик, Прага, Пломбирный, Красный бархат.
• Дизайн должен подходить для линейки продуктов в которой будут Прага, Медовик, Пломбирный, Тирамису, Красный бархат.
• Должен быть базовый цвет упаковки или ключевых элементов. При работе с линейкой вкусов будет изменяться базовый цвет.
• Основным элементом должно быть написание категорийного имени ТИРАМИСУ. Предпочтительное написание заглавными буквами. Следует учесть, что продолжение линейки вкусов (ПРАГА, МЕДОВИК, ПЛОМБИРНЫЙ) будет в том же стиле написания.
• Написание наименований и фон должны быть контрастными.
• Бренд: Bright Spoon, логотип бренда на усмотрение дизайнера, можно ограничиться только двумя заглавными буквами BS. Размер бренда должен быть меньше, чем название категории.
• Информация должна дублироваться на верхней и фронтальной части упаковки
• Форма обечайки может быть произвольной, но должен быть виден продукт по всей высоте по слоям, обечайка не должна закрывать весь продукт.
• В сочетании с дизайном обечайки продукт должен выглядеть как более аппетитный.
• Дизайн должен соответствовать ценовому позиционированию выше среднего средний плюс и увеличивать доверие к продукту.

```html
<!DOCTYPE html>
<html lang="ru">
<head>
<meta charset="utf-8">
<title>Bright Spoon — Тирамису, обечайка</title>
<link rel="stylesheet" href="https://fonts.googleapis.com/css2?family=Oswald:wght@600&family=PT+Serif&display=swap">
<style>
  :root {
    --page: #ffffff;
    --sleeve: #f4b7c8;
    --stripe: #f19db6;
    --badge: #f79cb9;
    --ring: #ffffff;
    --title: #8a2a17;
    --ink: #6e2416;
    --photo-top: #b0714a;
    --photo-mid: #f3eee6;
  }
  * { box-sizing: border-box; margin: 0; padding: 0; }
  html, body { width: 681px; height: 1200px; overflow: hidden; background: var(--page); }
  .canvas { position: relative; width: 681px; height: 1200px; }

  .sleeve {
    position: absolute;
    left: 201px;
    width: 272px;
    background: var(--sleeve);
  }
  .sleeve--top { top: 88px; height: 442px; }
  .sleeve--front { top: 625px; height: 522px; }

  .sleeve__stripes {
    position: absolute;
    left: 62px;
    width: 148px;
    top: 6px;
    bottom: 6px;
    background: repeating-linear-gradient(to bottom,
      var(--stripe) 0 5px, transparent 5px 11px);
    opacity: .8;
  }

  .badge {
    position: absolute;
    left: 50%;
    transform: translateX(-50%);
    border-radius: 50%;
    background: var(--badge);
    display: flex;
    flex-direction: column;
    align-items: center;
    text-align: center;
  }
  .badge::after {
    content: "";
    position: absolute;
    inset: 12px;
    border: 1px solid var(--ring);
    border-radius: 50%;
  }
  .sleeve--top .badge { top: 66px; width: 306px; height: 306px; padding-top: 82px; }
  .sleeve--front .badge { top: 125px; width: 276px; height: 276px; padding-top: 66px; }

  .badge__brand {
    font-family: "PT Serif", serif;
    font-size: 24px;
    color: var(--ink);
    line-height: 1;
  }
  .badge__name {
    font-family: "Oswald", sans-serif;
    font-weight: 600;
    font-size: 42px;
    letter-spacing: 1px;
    color: var(--title);
    line-height: 1;
    margin-top: 22px;
  }
  .badge__flavour {
    font-family: "PT Serif", serif;
    font-size: 16px;
    letter-spacing: .5px;
    color: var(--ink);
    margin-top: 14px;
  }
  .badge__photo {
    width: 58px;
    height: 58px;
    margin-top: 20px;
    border-radius: 4px;
    background: linear-gradient(to bottom, var(--photo-top) 0 30%, var(--photo-mid) 30% 48%, #c89a6a 48% 56%, var(--photo-mid) 56% 100%);
  }
  .sleeve--front .badge__name { font-size: 38px; margin-top: 20px; }
  .sleeve--front .badge__photo { margin-top: 18px; }
</style>
</head>
<body>
<main class="canvas">
  <section class="sleeve sleeve--top" aria-label="Обечайка, верх">
    <div class="sleeve__stripes"></div>
    <div class="badge">
      <p class="badge__brand">Bright Spoon</p>
      <h1 class="badge__name">ТИРАМИСУ</h1>
      <p class="badge__flavour">КОФЕЙНОЕ</p>
      <div class="badge__photo" role="img" aria-label="Фото пирожного тирамису"></div>
    </div>
  </section>

  <section class="sleeve sleeve--front" aria-label="Обечайка, бок">
    <div class="sleeve__stripes"></div>
    <div class="badge">
      <p class="badge__brand">Bright Spoon</p>
      <h2 class="badge__name">ТИРАМИСУ</h2>
      <p class="badge__flavour">КОФЕЙНОЕ</p>
      <div class="badge__photo" role="img" aria-label="Фото пирожного тирамису"></div>
    </div>
  </section>
</main>
</body>
</html>
```